Business Card- Occupational Therapist

I need business cards for Bright Harbour KidMotion, I am an Occupational Therapist offering child centred play therapy.
I am a sole private practitioner offering play therapy services to families in rural Great Southern region of WA, my mission statement is "Supporting country kids and families to grow"
This is a new business so I am needing to promote the value of child centred play therapy within the community, and my referrers (target audience) will be: rural GPs (doctors), child health nurse, schools, disability providers, child protection workers etc) but also the families of young children in rural areas.
Target Market(s)
Families of children
Referrers (Doctors, child health nurse, schools, disability providers, child protection workers)
Industry/Entity Type
Mental Health
Contact Information for Business Card
Maren Koltwick
Occupational Therapist
Phone: 0471 828 305
Email: maren@bhkidmotion.com.au
PO Box 71 | WARRENDALE WA 6418
Requirements
Must have
- Include Bright Harbour KidMotion logo and my contact details.
Include my credentials as an Occupational Therapist and Child Centred Play Therapist
Nice to have
- "Play is a child's language and toys are their words" Dorian Welkmore

```html
<!DOCTYPE html>
<html lang="en">
<head>
<meta charset="utf-8">
<title>Bright Harbour KidMotion – Business Card</title>
<link rel="stylesheet" href="https://fonts.googleapis.com/css2?family=Quicksand:wght@500&family=Roboto:wght@400;700&display=swap">
<style>
  :root {
    --purple: #5c1858;
    --purple-soft: #6a2466;
    --green: #249a2c;
    --green-deep: #2f7a35;
    --ink: #1d1d1d;
    --paper: #f4f4f4;
    --paper-shade: #dcdcdc;
    --backdrop: #e9e9e9;
    --light-text: #ececec;
  }
  html, body {
    margin: 0;
    width: 1200px;
    height: 1138px;
    overflow: hidden;
    background: var(--backdrop);
  }
  .card {
    position: absolute;
    left: 275px;
    width: 622px;
    height: 376px;
    border-radius: 16px;
    overflow: hidden;
    box-shadow: 0 6px 14px rgba(0,0,0,0.25);
  }
  /* Front */
  .card--front {
    top: 185px;
    background: linear-gradient(110deg, var(--purple) 0%, var(--purple-soft) 30%, #4a4a4a 50%, var(--green-deep) 75%, var(--green) 100%);
  }
  .front__name {
    position: absolute;
    top: 126px;
    left: 0;
    right: 0;
    margin: 0;
    text-align: center;
    font: 500 50px/56px "Quicksand", sans-serif;
    color: #f2f2f2;
  }
  .front__tagline {
    position: absolute;
    top: 342px;
    left: 0;
    right: 0;
    display: flex;
    justify-content: center;
    align-items: center;
    gap: 12px;
    font: 400 16px/20px "Roboto", sans-serif;
    color: var(--light-text);
  }
  .front__tagline::before,
  .front__tagline::after {
    content: "";
    width: 56px;
    height: 1.5px;
    background: var(--light-text);
  }
  /* Back */
  .card--back {
    top: 608px;
    background: linear-gradient(135deg, var(--paper) 0%, #ececec 55%, var(--paper-shade) 100%);
  }
  .back__brand {
    position: absolute;
    left: 40px;
    top: 82px;
    width: 240px;
    text-align: center;
  }
  .back__brand-name {
    margin: 0;
    font: 500 27px/31px "Quicksand", sans-serif;
    color: var(--ink);
  }
  .back__brand-dot {
    display: block;
    width: 62px;
    height: 62px;
    margin: 26px auto 0;
    border-radius: 50%;
    background: var(--green);
  }
  .back__details {
    position: absolute;
    left: 334px;
    top: 80px;
    font-family: "Roboto", sans-serif;
    color: var(--ink);
  }
  .person__name {
    margin: 0;
    font: 700 25px/30px "Roboto", sans-serif;
  }
  .person__first { color: var(--purple); }
  .person__last { color: var(--green-deep); }
  .person__role {
    margin: 2px 0 0;
    font-size: 16px;
    line-height: 20px;
  }
  .contact {
    list-style: none;
    margin: 30px 0 0;
    padding: 0;
    font-size: 17px;
    line-height: 24px;
  }
  .contact li {
    display: flex;
    align-items: center;
    gap: 16px;
  }
  .contact svg { width: 15px; height: 15px; flex: none; }
  .address {
    margin: 8px 0 0;
    font-size: 17px;
    line-height: 22px;
  }
  .back__bands {
    position: absolute;
    left: 0;
    bottom: 0;
    width: 622px;
    height: 47px;
  }
  .back__tagline {
    position: absolute;
    left: 270px;
    bottom: 13px;
    font: 400 16px/20px "Roboto", sans-serif;
    color: #f2e9f1;
  }
</style>
</head>
<body>
  <section class="card card--front">
    <h1 class="front__name">Bright Harbour<br>KidMotion</h1>
    <div class="front__tagline">Supporting country kids and families to grow</div>
  </section>

  <section class="card card--back">
    <div class="back__brand">
      <p class="back__brand-name">Bright Harbour<br>KidMotion</p>
      <span class="back__brand-dot"></span>
    </div>

    <div class="back__details">
      <h2 class="person__name"><span class="person__first">Maren</span> <span class="person__last">Koltwick</span></h2>
      <p class="person__role">Occupational Therapist</p>
      <ul class="contact">
        <li>
          <svg viewBox="0 0 16 16" aria-hidden="true"><path fill="#249a2c" d="M1 5c0-2 3-3 7-3s7 1 7 3v1h-3V5H4v1H1zM4 7h8l2 7H2z"/></svg>
          0471 828 305
        </li>
        <li>
          <svg viewBox="0 0 16 16" aria-hidden="true"><rect x="1" y="3" width="14" height="10" fill="#5c1858"/><path d="M1 3l7 6 7-6M1 13l5-5M15 13l-5-5" stroke="#fff" stroke-width="1.2" fill="none"/></svg>
          maren@bhkidmotion.com.au
        </li>
        <li>
          <svg viewBox="0 0 16 16" aria-hidden="true"><circle cx="8" cy="8" r="7" fill="#249a2c"/><path d="M1 8h14M8 1v14M3 4h10M3 12h10" stroke="#fff" stroke-width="0.9" fill="none"/></svg>
          www.bhkidmotion.com.au
        </li>
      </ul>
      <p class="address">PO Box 71 | WARRENDALE WA 6418</p>
    </div>

    <svg class="back__bands" viewBox="0 0 622 47" preserveAspectRatio="none" aria-hidden="true">
      <rect x="0" y="33" width="230" height="14" fill="var(--green)"/>
      <path d="M218 47 L236 0 H622 V47 Z" fill="var(--purple)"/>
    </svg>
    <div class="back__tagline">Supporting country kids &amp; families to grow</div>
  </section>
</body>
</html>
```